Bref créative
Business Cards and Stationary for Real Estate Firm
Maple Crest Realty Group
Professional
Dennis R. Holloway
Broker/Owner
4782 Lantern Hill Rd
Suite 308
Petaluma, CA 95862
dholloway@brightharborfirm.com
www.maplecrestrealtygroup.net
DRE # 02947716
There should be a place for a photo of the agent on the front of the card, but can work fine if the agent does not put their photo on it. These card designs will be used for multiple agents, I assume the name, phone numbers, email address, etc can be changed for each agent. The AI files and any others that may be needed are in the uploaded zip file.
The back of the card may be a tag line or some other kind of message.
Files in black and white, and with color.

```html
<!DOCTYPE html>
<html lang="en">
<head>
<meta charset="utf-8">
<title>Maple Crest Realty Group – Business Card</title>
<link href="https://fonts.googleapis.com/css2?family=Cinzel:wght@400&family=Josefin+Sans:wght@300;400&display=swap" rel="stylesheet">
<style>
  :root {
    --bg: #e4e2de;
    --red: #c8161d;
    --red-dark: #8f0d12;
    --red-light: #e0262c;
    --white: #ffffff;
    --ink: #3a3a3a;
    --muted: #6e6e6e;
    --rule: #c9c9c9;
  }
  * { box-sizing: border-box; margin: 0; padding: 0; }
  html, body { width: 1200px; height: 904px; overflow: hidden; }
  body {
    background: var(--bg);
    position: relative;
    font-family: "Josefin Sans", sans-serif;
  }
  .card {
    position: absolute;
    width: 700px;
    height: 400px;
    border-radius: 20px;
    box-shadow: 0 10px 24px rgba(0,0,0,0.18);
    overflow: hidden;
  }
  /* Back side */
  .card-back {
    left: 110px; top: 36px;
    background: radial-gradient(circle at 40% 35%, var(--red-light), var(--red) 55%, var(--red-dark));
    display: flex; flex-direction: column; align-items: center; justify-content: center;
    color: var(--white);
  }
  .card-back .brand {
    font-family: "Cinzel", serif;
    font-size: 34px;
    letter-spacing: 3px;
    color: var(--white);
  }
  .card-back .web {
    margin-top: 30px;
    font-size: 17px;
    letter-spacing: 3px;
    font-weight: 300;
  }
  /* Front side */
  .card-front {
    left: 390px; top: 468px;
    background: var(--white);
  }
  .front-brand {
    position: absolute; left: 40px; top: 96px; width: 300px;
    text-align: center;
    font-family: "Cinzel", serif;
    font-size: 27px;
    line-height: 1.25;
    letter-spacing: 2px;
    color: var(--red);
  }
  .agent {
    position: absolute; left: 70px; top: 262px;
  }
  .agent-name {
    font-size: 24px; color: var(--red); font-weight: 400;
  }
  .agent-title {
    margin-top: 6px; font-size: 16px; color: var(--muted); font-weight: 300; padding-left: 40px;
  }
  .divider {
    position: absolute; left: 372px; top: 88px; width: 1px; height: 240px; background: var(--rule);
  }
  .contact {
    position: absolute; left: 396px; top: 92px;
    font-size: 15px; line-height: 22px; color: var(--ink); font-weight: 300;
    list-style: none;
  }
  .contact li { display: flex; align-items: center; gap: 8px; white-space: nowrap; }
  .contact .gap { height: 8px; }
  .contact svg { width: 13px; height: 13px; fill: var(--red); flex: none; }
  .contact .plain { padding-left: 21px; }
  .contact .address { padding-left: 0; }
</style>
</head>
<body>
  <section class="card card-back">
    <div class="brand">Maple Crest Realty Group</div>
    <div class="web">www.maplecrestrealtygroup.net</div>
  </section>

  <section class="card card-front">
    <div class="front-brand">Maple Crest<br>Realty Group</div>
    <div class="agent">
      <div class="agent-name">Dennis R. Holloway</div>
      <div class="agent-title">Broker/Owner</div>
    </div>
    <div class="divider"></div>
    <ul class="contact">
      <li class="address">4782 Lantern Hill Rd</li>
      <li class="address">Suite 308</li>
      <li class="address">Petaluma, CA 95862</li>
      <li class="gap"></li>
      <li><svg viewBox="0 0 24 24"><path d="M6.6 10.8a15.1 15.1 0 0 0 6.6 6.6l2.2-2.2c.3-.3.7-.4 1-.2 1.1.4 2.3.6 3.6.6.6 0 1 .4 1 1V20c0 .6-.4 1-1 1A17 17 0 0 1 3 4c0-.6.4-1 1-1h3.5c.6 0 1 .4 1 1 0 1.3.2 2.5.6 3.6.1.3 0 .7-.2 1z"/></svg>(415) 555-0187</li>
      <li><svg viewBox="0 0 24 24"><rect x="6" y="1" width="12" height="22" rx="2"/></svg>(707) 555-0142</li>
      <li><svg viewBox="0 0 24 24"><rect x="3" y="5" width="18" height="14" rx="1"/></svg>(888) 555-0163</li>
      <li><svg viewBox="0 0 24 24"><path d="M2 5h20v14H2z M2 5l10 8 10-8" /></svg>dholloway@brightharborfirm.com</li>
      <li><svg viewBox="0 0 24 24"><circle cx="12" cy="12" r="10"/></svg>www.maplecrestrealtygroup.net</li>
    </ul>
  </section>
</body>
</html>
```